Medical clinic Flyer for Tovren Medical clinic in Chilliwack, BC

Need a double sided flyer design sized 5.5" x 8.5'' for a medical clinic. The flyer attached for Marlow Crest clinic is a good example of what we are looking for.

We need to focus on advertising this clinic as being a walk in clinic with short wait time. We need to make "walk in clinic Now open" eye catching.

We need to include the following messages:
1. Full Family Practice.
2. Accepting new patients.
3. Walk in clinic open Monday to Friday 9am to 4pm.
4. Short wait times.
5. No appointment needed
6.Check out our state of the art Medical clinic.
7. Velnox, Dermal Fillers, and Corvessa available (Physician Lead)

Target Market(s)

Residents of Chilliwack, BC.

Industry/Entity Type

Healthcare

Requirements
Must have
• Phone number: 18775206348
Addres: 4519 Birchwold Trail Pkwy Unit#312, Chilliwack, BC, V2R 0K7
Nice to have
• Location Map

```html
<!DOCTYPE html>
<html lang="en">
<head>
<meta charset="utf-8">
<title>Tovren Medical Centre – Walk In Clinic Flyer</title>
<link href="https://fonts.googleapis.com/css2?family=Bebas+Neue&family=Nunito+Sans:wght@400;600;700&display=swap" rel="stylesheet">
<style>
  :root {
    --navy: #1f3f7a;
    --blue: #3a4b9a;
    --blue-deep: #28357e;
    --red: #c8202f;
    --red-deep: #b3192a;
    --white: #ffffff;
    --ink: #2b2b2b;
    --page: #efeceb;
    --photo-light: #e4e2dc;
    --photo-mid: #c9c6bf;
  }
  * { margin: 0; padding: 0; box-sizing: border-box; }
  html, body { width: 1200px; height: 1200px; overflow: hidden; background: var(--page); }
  body { position: relative; font-family: "Nunito Sans", Arial, sans-serif; }

  .flyer {
    position: absolute;
    left: 166px;
    width: 918px;
    height: 592px;
    background: var(--white);
    overflow: hidden;
    transform-origin: 0 0;
    transform: scale(0.9455);
    box-shadow: 0 4px 14px rgba(0,0,0,0.18);
  }
  .flyer--front { top: 26px; }
  .flyer--back { top: 614px; }
  .shapes { position: absolute; inset: 0; }
  .layer { position: absolute; }

  /* brand */
  .brand { display: flex; align-items: center; gap: 14px; color: var(--red); font-weight: 700; }
  .brand-dot { width: 46px; height: 46px; border-radius: 50%; background: var(--red); flex: none; }
  .brand-name { line-height: 1; }
  .brand-name .line1 { display: block; font-size: 52px; letter-spacing: 1px; }
  .brand-name .line2 { display: block; font-size: 21px; letter-spacing: 1px; margin-top: 6px; }

  /* front */
  .front-brand { left: 40px; top: 46px; }
  .headline-walk {
    left: 38px; top: 176px;
    font-family: "Bebas Neue", Impact, sans-serif;
    font-size: 82px; line-height: 1; color: var(--navy); letter-spacing: 0.5px;
  }
  .headline-open {
    left: 0; top: 256px; width: 428px; height: 118px;
    background: var(--red);
    font-family: "Bebas Neue", Impact, sans-serif;
    font-size: 122px; line-height: 128px; color: var(--white); padding-left: 34px; letter-spacing: 1px;
  }
  .phone-row { display: flex; align-items: center; gap: 12px; }
  .phone-icon { width: 46px; height: 46px; flex: none; }
  .front-phone { left: 32px; top: 452px; color: var(--white); font-size: 54px; font-weight: 600; letter-spacing: -0.5px; }
  .front-address { left: 94px; top: 518px; color: var(--white); font-size: 17.5px; font-weight: 600; line-height: 1.25; }

  /* back */
  .service-title { left: 42px; top: 6px; color: var(--white); font-size: 34px; font-weight: 600; display: flex; align-items: center; gap: 8px; }
  .service-title svg { width: 36px; height: 36px; }
  .service-list { left: 42px; top: 70px; list-style: none; width: 420px; }
  .service-list li { display: flex; align-items: flex-start; gap: 12px; color: var(--white); font-size: 15px; line-height: 1.2; height: 45px; }
  .service-list li .tick { width: 34px; height: 34px; flex: none; margin-top: -6px; }
  .service-list li span { padding-top: 2px; }
  .back-address { left: 515px; top: 340px; color: var(--white); font-size: 17.5px; line-height: 1.25; display: flex; gap: 10px; }
  .back-address svg { width: 20px; height: 24px; flex: none; margin-top: 2px; }
  .back-phone { left: 498px; top: 416px; color: var(--red); font-size: 54px; font-weight: 600; letter-spacing: -0.5px; }
  .back-brand { left: 555px; top: 498px; }
  .back-brand .brand-name .line1 { font-size: 46px; }
  .back-brand .brand-name .line2 { font-size: 19px; }
</style>
</head>
<body>

<section class="flyer flyer--front" aria-label="Flyer front">
  <svg class="shapes" viewBox="0 0 918 592" width="918" height="592">
    <defs>
      <linearGradient id="frontBlue" x1="0" y1="0" x2="0" y2="1">
        <stop offset="0" stop-color="#4352a2"/>
        <stop offset="1" stop-color="#27347c"/>
      </linearGradient>
      <linearGradient id="roomPhoto" x1="0" y1="0" x2="1" y2="1">
        <stop offset="0" stop-color="#ecebe5"/>
        <stop offset="0.6" stop-color="#d9d7d0"/>
        <stop offset="1" stop-color="#b9b7b2"/>
      </linearGradient>
      <linearGradient id="cityFade" x1="0" y1="0" x2="0" y2="1">
        <stop offset="0" stop-color="#f4f4f6"/>
        <stop offset="1" stop-color="#dcdde2"/>
      </linearGradient>
    </defs>
    <rect x="0" y="0" width="918" height="592" fill="#fbfbfb"/>
    <g role="img" aria-label="Faint city skyline backdrop">
      <rect x="0" y="374" width="560" height="62" fill="url(#cityFade)"/>
    </g>
    <rect x="0" y="436" width="620" height="156" fill="url(#frontBlue)"/>
    <path d="M542 0 H918 V592 H548 C470 480 452 310 500 180 C520 110 540 50 558 0 Z" fill="var(--red)"/>
    <g role="img" aria-label="Photo of a clinic examination room with exam bed, chair and computer desk">
      <path d="M566 0 H918 V592 H575 C492 480 472 310 520 180 C540 110 560 50 578 0 Z" fill="url(#roomPhoto)"/>
    </g>
  </svg>

  <div class="layer brand front-brand">
    <span class="brand-dot"></span>
    <span class="brand-name"><span class="line1">TOVREN</span><span class="line2">MEDICAL CENTRE</span></span>
  </div>

  <div class="layer headline-walk">WALK IN CLINIC</div>
  <div class="layer headline-open">NOW OPEN</div>

  <div class="layer phone-row front-phone">
    <svg class="phone-icon" viewBox="0 0 46 46" aria-hidden="true">
      <circle cx="23" cy="23" r="23" fill="var(--red)"/>
      <path d="M17 12c2-1 3 0 4 2l1 4c0 1-1 2-2 3 1 3 3 5 5 7 1-1 2-2 3-2l4 1c2 1 2 3 1 4l-2 2c-6 1-16-9-16-17z" fill="var(--white)"/>
    </svg>
    <span>18775206348</span>
  </div>
  <div class="layer front-address">4519 Birchwold Trail Pkwy Unit#312,<br>Chilliwack, BC, V2R 0K7</div>
</section>

<section class="flyer flyer--back" aria-label="Flyer back">
  <svg class="shapes" viewBox="0 0 918 592" width="918" height="592">
    <defs>
      <linearGradient id="backBlue" x1="0" y1="0" x2="0" y2="1">
        <stop offset="0" stop-color="#3f4f9f"/>
        <stop offset="1" stop-color="#2b3881"/>
      </linearGradient>
      <linearGradient id="lobbyPhoto" x1="0" y1="0" x2="1" y2="1">
        <stop offset="0" stop-color="#5a5a5a"/>
        <stop offset="0.5" stop-color="#b9b4aa"/>
        <stop offset="1" stop-color="#d9d5cc"/>
      </linearGradient>
      <linearGradient id="mapTone" x1="0" y1="0" x2="1" y2="1">
        <stop offset="0" stop-color="#e6e8ec"/>
        <stop offset="1" stop-color="#c9d6ee"/>
      </linearGradient>
    </defs>
    <rect width="918" height="592" fill="var(--white)"/>
    <rect x="0" y="52" width="470" height="353" fill="url(#backBlue)"/>
    <path d="M0 0 H400 L425 52 H0 Z" fill="var(--red)"/>
    <g role="img" aria-label="Photo of the clinic reception desk and pharmacy counter">
      <rect x="0" y="410" width="460" height="182" fill="url(#lobbyPhoto)"/>
    </g>
    <path d="M398 0 H440 C480 90 500 240 472 360 C450 460 390 540 330 592 H300 C360 540 420 470 445 380 C470 290 460 160 420 52 Z" fill="var(--white)"/>
    <path d="M400 0 C455 80 490 230 466 360 C446 460 390 540 318 592 H346 C420 540 470 460 484 360 C500 240 470 90 425 0 Z" fill="var(--red)"/>
    <rect x="478" y="292" width="440" height="108" fill="url(#backBlue)"/>
    <rect x="498" y="22" width="398" height="304" fill="var(--white)"/>
    <g role="img" aria-label="Location map of the clinic area in Chilliwack">
      <rect x="505" y="29" width="384" height="290" fill="url(#mapTone)"/>
    </g>
  </svg>

  <div class="layer service-title">
    <svg viewBox="0 0 36 36" aria-hidden="true">
      <path d="M6 30 L22 14 M4 8 L28 32" stroke="var(--white)" stroke-width="5" stroke-linecap="round" fill="none"/>
      <circle cx="25" cy="10" r="6" fill="none" stroke="var(--white)" stroke-width="3.5"/>
    </svg>
    <span>Our service</span>
  </div>

  <ul class="layer service-list">
    <li><svg class="tick" viewBox="0 0 34 34" aria-hidden="true"><circle cx="17" cy="17" r="15" fill="var(--white)"/><path d="M10 17 l5 5 l10 -11" stroke="var(--red)" stroke-width="3.5" fill="none" stroke-linecap="round" stroke-linejoin="round"/></svg><span>Full Family Practice.</span></li>
    <li><svg class="tick" viewBox="0 0 34 34" aria-hidden="true"><circle cx="17" cy="17" r="15" fill="var(--white)"/><path d="M10 17 l5 5 l10 -11" stroke="var(--red)" stroke-width="3.5" fill="none" stroke-linecap="round" stroke-linejoin="round"/></svg><span>Accepting new patients.</span></li>
    <li><svg class="tick" viewBox="0 0 34 34" aria-hidden="true"><circle cx="17" cy="17" r="15" fill="var(--white)"/><path d="M10 17 l5 5 l10 -11" stroke="var(--red)" stroke-width="3.5" fill="none" stroke-linecap="round" stroke-linejoin="round"/></svg><span>Walk in clinic open Monday to Friday 9am to 4pm.</span></li>
    <li><svg class="tick" viewBox="0 0 34 34" aria-hidden="true"><circle cx="17" cy="17" r="15" fill="var(--white)"/><path d="M10 17 l5 5 l10 -11" stroke="var(--red)" stroke-width="3.5" fill="none" stroke-linecap="round" stroke-linejoin="round"/></svg><span>Short wait times.</span></li>
    <li><svg class="tick" viewBox="0 0 34 34" aria-hidden="true"><circle cx="17" cy="17" r="15" fill="var(--white)"/><path d="M10 17 l5 5 l10 -11" stroke="var(--red)" stroke-width="3.5" fill="none" stroke-linecap="round" stroke-linejoin="round"/></svg><span>No appointment needed</span></li>
    <li><svg class="tick" viewBox="0 0 34 34" aria-hidden="true"><circle cx="17" cy="17" r="15" fill="var(--white)"/><path d="M10 17 l5 5 l10 -11" stroke="var(--red)" stroke-width="3.5" fill="none" stroke-linecap="round" stroke-linejoin="round"/></svg><span>Check out our state of the art Medical clinic.</span></li>
    <li><svg class="tick" viewBox="0 0 34 34" aria-hidden="true"><circle cx="17" cy="17" r="15" fill="var(--white)"/><path d="M10 17 l5 5 l10 -11" stroke="var(--red)" stroke-width="3.5" fill="none" stroke-linecap="round" stroke-linejoin="round"/></svg><span>Velnox, Dermal Fillers, and Corvessa available<br>(Physician Lead)</span></li>
  </ul>

  <div class="layer back-address">
    <svg viewBox="0 0 20 24" aria-hidden="true"><path d="M10 1a8 8 0 0 0-8 8c0 6 8 14 8 14s8-8 8-14a8 8 0 0 0-8-8z" fill="none" stroke="var(--white)" stroke-width="2"/><circle cx="10" cy="9" r="3" fill="none" stroke="var(--white)" stroke-width="2"/></svg>
    <span>4519 Birchwold Trail Pkwy Unit#312,<br>Chilliwack, BC, V2R 0K7</span>
  </div>

  <div class="layer phone-row back-phone">
    <svg class="phone-icon" viewBox="0 0 46 46" aria-hidden="true">
      <circle cx="23" cy="23" r="23" fill="var(--red)"/>
      <path d="M17 12c2-1 3 0 4 2l1 4c0 1-1 2-2 3 1 3 3 5 5 7 1-1 2-2 3-2l4 1c2 1 2 3 1 4l-2 2c-6 1-16-9-16-17z" fill="var(--white)"/>
    </svg>
    <span>18775206348</span>
  </div>

  <div class="layer brand back-brand">
    <span class="brand-dot"></span>
    <span class="brand-name"><span class="line1">TOVREN</span><span class="line2">MEDICAL CENTRE</span></span>
  </div>
</section>

</body>
</html>
```